KESTRA FLOW SUPPLY business card

We need a new business card for our company "Kestra Flow Supply". The company is very simple, we supply bulk heated water to the oilfield and industry. I have included a few images of cards that I like so that you have an idea of the direction I want to go. I will leave fonts up to the designer. I have also included our logo.
Updates

Hello Designers,  if there are any more submissions coming in you might consider using other background colors than black.  I am looking for a little bit of variety before making the decision.

Thanks,

Dale

Sorry, I meant to say background colors other than just black and white.

Thanks,

Dale

Target Market(s)

Ages 20 to 60. Oilfield consultants and Oil and Gas Companies

Industry/Entity Type

Business

Font styles to use
Sans Serif

Requirements
Must have
• Dale Fenwick

email info@kestraflowsupply.example

Phone # 555-318-2047
Fax 555-376-9150

Site 713, Box 2, Comp 4, RR3
Corran Flats, WP, X9Z 4Q8

3-17-52-4 W4M
Hwy 905 Between RR37 & RR38

**Must have our logo

Nice to have
• Would be nice to have " Bulk Heated Water" somewhere on the card

The logo with the flame large across the background might look ok? The name of the company is KESTRA FLOW SUPPLY, but it probably isn't necessary to have the hot water under the logo all the time if you decide it looks better. As long as it is included somewhere on the card. The style of the KESTRA can change slightly (ie:; can be slanted).

The colors of the logo can change, but it might be nice to have the original color and logo somewhere small (corner?)

```html
<!DOCTYPE html>
<html lang="en">
<head>
<meta charset="utf-8">
<title>Kestra Flow Supply – Business Card</title>
<link rel="stylesheet" href="https://fonts.googleapis.com/css2?family=Arimo:wght@400;700&display=swap">
<style>
  :root {
    --backdrop-light: #ffffff;
    --backdrop-edge: #e6e7e8;
    --charcoal: #3e3e3f;
    --charcoal-dark: #383839;
    --charcoal-sheen: #4a4a4b;
    --brand-blue: #1f86c0;
    --brand-red: #e21f26;
    --red-light: #ec2227;
    --red-dark: #c8161d;
    --white: #ffffff;
    --divider: rgba(255,255,255,0.45);
  }
  * { margin: 0; padding: 0; box-sizing: border-box; }
  html, body { width: 1200px; height: 1001px; overflow: hidden; }
  body {
    position: relative;
    font-family: "Arimo", Arial, sans-serif;
    background: var(--backdrop-light);
    color: var(--white);
  }
  .stage {
    position: absolute; left: 0; top: 0; width: 1200px; height: 591px;
    background: radial-gradient(ellipse 60% 60% at 50% 50%, var(--backdrop-light) 40%, var(--backdrop-edge) 100%);
  }
  .card {
    position: absolute; top: 167px; width: 552px; height: 318px; overflow: hidden;
  }
  .card-front {
    left: 37px;
    background: linear-gradient(180deg, var(--charcoal-dark) 0%, var(--charcoal) 45%, var(--charcoal-sheen) 58%, var(--charcoal) 70%, var(--charcoal-dark) 100%);
  }
  .card-front .top-band {
    position: absolute; left: 0; top: 0; width: 100%; height: 13px; background: var(--brand-blue);
  }
  .lockup { position: absolute; display: flex; align-items: center; white-space: nowrap; }
  .wordmark {
    display: flex; align-items: center; gap: 6px;
    font-weight: 700; color: var(--brand-red); letter-spacing: 0.01em; line-height: 1;
  }
  .wordmark .dot { border-radius: 50%; background: var(--brand-blue); flex: none; }
  .lockup .rule { width: 1px; background: var(--divider); flex: none; }
  .tagline { font-weight: 400; color: var(--white); white-space: nowrap; }

  .card-front .lockup { left: 139px; top: 146px; }
  .card-front .wordmark { font-size: 24px; }
  .card-front .wordmark .dot { width: 12px; height: 12px; }
  .card-front .rule { height: 48px; margin: 0 14px; }
  .card-front .tagline { font-size: 12.5px; }

  .card-back {
    left: 611px;
    background: linear-gradient(180deg, var(--red-light) 0%, var(--brand-red) 55%, var(--red-dark) 100%);
  }
  .contact { position: absolute; left: 320px; top: 116px; }
  .contact .name { font-size: 31px; font-weight: 400; line-height: 1; margin-bottom: 13px; }
  .contact .line { font-size: 13.5px; line-height: 20px; }
  .contact .block + .block { margin-top: 17px; }
  .contact-bar {
    position: absolute; left: 12px; right: 14px; top: 292px;
    display: flex; justify-content: space-between; align-items: center;
    font-size: 14.5px; white-space: nowrap;
  }
  .contact-bar .item { display: flex; align-items: center; }
  .contact-bar .sep { width: 1px; height: 14px; background: var(--white); margin: 0 9px; }
  .contact-bar svg { display: block; }

  .showcase {
    position: absolute; left: 545px; top: 591px; width: 655px; height: 410px;
    background: linear-gradient(180deg, var(--charcoal-dark) 0%, var(--charcoal) 40%, var(--charcoal-sheen) 58%, var(--charcoal) 75%, var(--charcoal-dark) 100%);
  }
  .showcase .lockup { left: 93px; top: 219px; }
  .showcase .wordmark { font-size: 46px; gap: 10px; }
  .showcase .wordmark .dot { width: 22px; height: 22px; }
  .showcase .rule { height: 96px; margin: 0 31px; }
  .showcase .tagline { font-size: 23px; }
</style>
</head>
<body>
  <section class="stage">
    <article class="card card-front">
      <div class="top-band"></div>
      <div class="lockup">
        <div class="wordmark"><span class="dot"></span>KESTRA</div>
        <div class="rule"></div>
        <div class="tagline">Bulk Heated Water</div>
      </div>
    </article>

    <article class="card card-back">
      <div class="contact">
        <h1 class="name">Dale Fenwick</h1>
        <div class="block">
          <p class="line">Site 713, Box 2, Comp 4, RR3</p>
          <p class="line">Corran Flats, WP, X9Z 4Q8</p>
        </div>
        <div class="block">
          <p class="line">3-17-52-4 W4M</p>
          <p class="line">Hwy 905 Between RR37 &amp; RR38</p>
        </div>
      </div>
      <div class="contact-bar">
        <div class="item">
          <svg width="15" height="11" viewBox="0 0 15 11" aria-label="Email"><rect x="0.5" y="0.5" width="14" height="10" fill="none" stroke="#fff"/><path d="M0.5 0.5 L7.5 6 L14.5 0.5" fill="none" stroke="#fff"/></svg>
          <span class="sep"></span><span>info@kestraflowsupply.example</span>
        </div>
        <div class="item">
          <svg width="15" height="12" viewBox="0 0 15 12" aria-label="Phone"><path d="M1 4 C1 1 14 1 14 4 L11 5 L10 3 L5 3 L4 5 Z" fill="#fff"/><rect x="3" y="6" width="9" height="5" rx="1" fill="none" stroke="#fff"/></svg>
          <span class="sep"></span><span>555-318-2047</span>
        </div>
        <div class="item">
          <svg width="20" height="12" viewBox="0 0 20 12" aria-label="Fax"><rect x="0.5" y="0.5" width="19" height="11" fill="none" stroke="#fff"/><text x="10" y="9" font-size="8" fill="#fff" text-anchor="middle" font-family="Arimo, Arial, sans-serif">Fax</text></svg>
          <span class="sep"></span><span>555-376-9150</span>
        </div>
      </div>
    </article>
  </section>

  <section class="showcase">
    <div class="lockup">
      <div class="wordmark"><span class="dot"></span>KESTRA</div>
      <div class="rule"></div>
      <div class="tagline">Bulk Heated Water</div>
    </div>
  </section>
</body>
</html>
```